Webdesign für Gemeinschaftspraxis (13820)
Zielgruppe
Die Website ist für eine fachärztliche Gemeinschaftspraxis, die sich aus Internisten, Betriebsmedizinern, Präventionsärzten, Kardiologen, Allgemeinmedizinern und Phlebologen zusammensetzt.
Die Zielgruppe sind bestehende Patienten sowie potentielle Patienten.
Die Website soll informativ sein.
Aufgabenstellung
Die Website soll in schlichten Farben gehalten sein, die zum Logo und zu den Fotos passen.
Die Website soll als kurzer, informativer Auftritt dienen
Die gelieferten Fotos sollen verwendet werden.
Es soll eine Onepage-Website werden, die so aufgebaut ist, wie die Website unter dem folgenden Link: https://www.kolbenfeld-portal.de/

```html
<!DOCTYPE html>
<html lang="de">
<head>
<meta charset="utf-8">
<title>Gemeinschaftspraxis am Lindenhof</title>
<link rel="stylesheet" href="https://fonts.googleapis.com/css2?family=Montserrat:wght@300;400;500;600&family=Oswald:wght@300;400&family=Roboto+Slab:wght@300;400&family=Raleway:wght@300;400;600&display=swap">
<style>
:root{
  --brown:#9a6548;
  --navy:#1f2e5c;
  --link:#3b77b3;
  --line:#e6e6e6;
  --grey-card:#f0f0f0;
  --blue-band:#33508a;
  --blue-deep:#28427a;
  --green:#93d57e;
  --orange:#ef8534;
  --salmon:#f3a676;
  --text:#444;
  --footer-bg:#f6f7fa;
}
*{box-sizing:border-box;margin:0;padding:0}
html,body{width:1200px;height:4162px;overflow:hidden;background:#fff;color:var(--text);font-family:'Raleway',sans-serif}
.page{position:relative;width:1200px;height:4162px}

/* header */
.site-header{position:absolute;top:0;left:0;width:1200px;height:174px;border-bottom:1px solid #8a7a70}
.brand{position:absolute;top:18px;left:0;width:1200px;text-align:center}
.brand-mark{display:inline-block;width:14px;height:14px;background:var(--navy);vertical-align:middle;margin-right:10px}
.brand-name{font-family:'Montserrat',sans-serif;font-weight:600;font-size:24px;color:var(--navy);vertical-align:middle;letter-spacing:.5px}
.brand-sub{display:block;margin-top:12px;font-family:'Montserrat',sans-serif;font-size:11px;color:var(--navy);letter-spacing:1px}
.main-nav{position:absolute;top:134px;left:0;width:1200px;text-align:center;font-family:'Oswald',sans-serif;font-weight:300;font-size:15px}
.main-nav a{color:var(--brown);text-decoration:none;margin:0 11px;text-transform:uppercase}
.search-btn{position:absolute;top:127px;left:1089px;width:47px;height:36px;background:#555;display:flex;align-items:center;justify-content:center}

/* hero */
.hero{position:absolute;top:175px;left:0;width:1200px;height:566px;background:linear-gradient(180deg,#e8e5e0 0%,#cfc6ba 45%,#d9d6d2 60%,#c3c7cc 100%)}
.hero-title{position:absolute;top:165px;width:1200px;text-align:center;font-family:'Montserrat',sans-serif;font-weight:400;font-size:46px;line-height:46px;color:#fff;text-shadow:0 1px 4px rgba(0,0,0,.35)}
.hero-text{position:absolute;top:280px;left:350px;width:500px;text-align:center;font-family:'Roboto Slab',serif;font-size:14px;line-height:21px;color:#fff;text-shadow:0 1px 3px rgba(0,0,0,.5)}
.slider-dots{position:absolute;top:510px;left:573px;display:flex;gap:7px}
.slider-dots span{width:13px;height:13px;border:2px solid #555;background:#fff}

/* treatments */
.section-title{font-family:'Montserrat',sans-serif;font-weight:400;font-size:30px;color:var(--brown);text-align:center;letter-spacing:.5px}
.treatments{position:absolute;top:810px;left:0;width:1200px}
.treatment-list{list-style:none;margin:50px 0 0 142px;width:917px}
.treatment-list li{height:57px;border-bottom:1px solid var(--line);font-family:'Roboto Slab',serif;font-weight:300;font-size:17px;color:var(--link);padding:14px 0 0 29px;position:relative}
.treatment-list li::before{content:"";position:absolute;left:12px;top:17px;border-left:6px solid #111;border-top:4px solid transparent;border-bottom:4px solid transparent}

/* team */
.team{position:absolute;top:2060px;left:0;width:1200px}
.team-intro{text-align:center;font-size:13px;margin-top:10px;color:#333}
.member{position:absolute;background:var(--grey-card);text-align:center}
.member-photo{display:block}
.member-name{font-family:'Montserrat',sans-serif;font-size:19px;color:#333}
.member-role{font-family:'Montserrat',sans-serif;font-size:11px;color:#999;margin-top:8px}
.mail-btn{display:inline-flex;width:32px;height:32px;background:#fff;align-items:center;justify-content:center;margin-top:12px}

/* hours */
.hours{position:absolute;top:2836px;left:0;width:1200px;height:936px;background:linear-gradient(180deg,var(--blue-deep),var(--blue-band) 60%,#3a5690)}
.hours-title{position:absolute;top:80px;width:1200px;text-align:center;font-family:'Montserrat',sans-serif;font-size:30px;color:#fff;letter-spacing:.5px}
.hours-intro{position:absolute;top:145px;width:1200px;text-align:center;font-size:13px;font-weight:300;color:#dfe4f0}
.timetable{position:absolute;top:210px;left:298px;width:604px;border-collapse:collapse;background:#fff;outline:3px solid #fff;font-family:'Montserrat',sans-serif;font-size:12.5px;color:#222;table-layout:fixed}
.timetable th{background:#7d8aa9;color:#fff;font-weight:400;text-align:left;padding:4px 3px;height:28px;border:1px solid #fff}
.timetable td{border:1px solid #c9c9c9;padding:1px 2px;line-height:19px;vertical-align:middle}
.timetable td.time{font-size:11.5px;padding-left:4px}
.free{background:var(--green)}
.visit{background:var(--salmon)}
.appt{background:var(--orange)}
.address-card{position:absolute;top:3496px;left:134px;width:933px;height:208px;background:rgba(130,150,190,.45);text-align:center;color:#dfe5f2}
.address-card h3{font-family:'Montserrat',sans-serif;font-weight:500;font-size:26px;color:#fff;margin-top:4px}
.address-card p{font-size:12px;font-weight:300;line-height:18px;margin-top:8px}

/* cta */
.cta{position:absolute;top:3772px;left:0;width:1200px;height:170px;background:#fff}
.cta-text{position:absolute;top:96px;left:134px;font-family:'Montserrat',sans-serif;font-weight:300;font-size:22px;color:#666}
.btn{position:absolute;top:96px;width:213px;height:32px;font-family:'Montserrat',sans-serif;font-weight:600;font-size:11px;display:flex;align-items:center;justify-content:center;text-transform:uppercase}
.btn-call{left:615px;background:var(--brown);color:#fff}
.btn-mail{left:845px;background:#fff;color:var(--brown);border:1px solid #eee;box-shadow:0 1px 3px rgba(0,0,0,.08)}

/* footer */
.site-footer{position:absolute;top:3942px;left:0;width:1200px;height:220px;background:var(--footer-bg);font-size:13px;color:#555}
.contact-list{position:absolute;top:78px;left:134px;list-style:none}
.contact-list li{height:28px;display:flex;align-items:center;gap:14px}
.footer-col{position:absolute;top:30px;text-align:right}
.footer-col h4{font-family:'Montserrat',sans-serif;font-weight:600;font-size:10px;color:#333;margin-bottom:18px;letter-spacing:.5px}
.footer-col ul{list-style:none}
.footer-col li{line-height:21px}
</style>
</head>
<body>
<div class="page">

<header class="site-header">
  <div class="brand">
    <span class="brand-mark"></span><span class="brand-name">Gemeinschaftspraxis am Lindenhof</span>
    <span class="brand-sub">Dr. Albers – Dr. Kühn – Wendt</span>
  </div>
  <nav class="main-nav">
    <a>Startseite</a><a>Behandlungen</a><a>Team</a><a>Öffnungszeiten</a><a>Kontakt</a>
  </nav>
  <div class="search-btn">
    <svg width="13" height="13" viewBox="0 0 13 13"><circle cx="5.5" cy="5.5" r="4" fill="none" stroke="#fff" stroke-width="2"/><line x1="8.5" y1="8.5" x2="12" y2="12" stroke="#fff" stroke-width="2"/></svg>
  </div>
</header>

<section class="hero" role="img" aria-label="Foto des hellen Praxisempfangs mit Holztresen und Wartebereich">
  <h1 class="hero-title">Willkommen in unserer<br>Gemeinschaftspraxis</h1>
  <p class="hero-text">Enim ad minim veniam, quis nostrud exercitation ullamco laboris nisi ut aliquip ex ea commodo conse quat. Duis aute irure dolor in reprehenderit in voluptate.</p>
  <div class="slider-dots"><span></span><span></span><span></span></div>
</section>

<section class="treatments">
  <h2 class="section-title">WELCHE BEHANDLUNGEN BIETEN WIR AN?</h2>
  <ul class="treatment-list">
    <li>Gesundheitsvorsorge/Prävention/Gesundheits-Check-up</li>
    <li>Impfungen und Reiseimpfungen</li>
    <li>Männervorsorge</li>
    <li>Diabetes mellitus</li>
    <li>Psychosomatische Grundversorgung</li>
    <li>Koronare Herzerkrankung (KHK)</li>
    <li>Asthma Bronchiale</li>
    <li>Palliativversorgung</li>
    <li>Prävention</li>
    <li>Echokardiografie</li>
    <li>Sonographische Untersuchung der Schilddrüse</li>
    <li>„Check-up“-Laboruntersuchungen sowie PSA-Wert und andere Tumormarker</li>
    <li>EKG und Belastungs-EKG</li>
    <li>Langzeit-Blutdruckmessung</li>
    <li>Disease-Management-Programme (DMP)</li>
    <li>Ultraschall der Bauchorgane</li>
    <li>Ultraschall der Hirnversorgenden Arterien (Duplexsonografie)</li>
    <li>Spiroergometrie</li>
  </ul>
</section>

<section class="team">
  <h2 class="section-title">PRAXISTEAM</h2>
  <p class="team-intro">Hier können Sie einen kurzen Text über Teambuilding oder ähnliches schreiben.</p>
  <div class="member" style="top:133px;left:142px;width:543px;height:525px">
    <div class="member-photo" role="img" aria-label="Gruppenfoto der drei Praxisärzte" style="width:543px;height:397px;background:linear-gradient(135deg,#3a3a3a,#1a1a1a 60%,#2b2b2b)"></div>
    <div style="padding-top:24px">
      <div class="member-name">Dr. Albers - Dr. Kühn - Wendt</div>
      <div class="member-role">Fachärzte für Innere Medizin</div>
      <span class="mail-btn"><svg width="11" height="8" viewBox="0 0 11 8"><rect width="11" height="8" fill="#777"/><path d="M0 0 L5.5 4.5 L11 0" stroke="#fff" fill="none"/></svg></span>
    </div>
  </div>
  <div class="member" style="top:235px;left:702px;width:357px;height:321px;background:transparent">
    <div class="member-photo" role="img" aria-label="Porträtfoto der Praxisassistentin" style="margin-left:81px;width:195px;height:194px;background:linear-gradient(160deg,#c9b29a,#6b4b3a 55%,#2f2a33)"></div>
    <div style="background:var(--grey-card);height:127px;padding-top:24px">
      <div class="member-name">Fr. Brandt</div>
      <div class="member-role">Praxisassistentin</div>
      <span class="mail-btn"><svg width="11" height="8" viewBox="0 0 11 8"><rect width="11" height="8" fill="#777"/><path d="M0 0 L5.5 4.5 L11 0" stroke="#fff" fill="none"/></svg></span>
    </div>
  </div>
</section>

<section class="hours">
  <h2 class="hours-title">UNSERE ÖFFNUNGSZEITEN</h2>
  <p class="hours-intro">Hier können Sie einen beliebigen Text zur Lokalität oder ähnlichem schreiben.</p>
  <table class="timetable">
    <colgroup><col style="width:87px"><col><col><col><col><col></colgroup>
    <tr><th>Zeit</th><th>Montag</th><th>Dienstag</th><th>Mittwoch</th><th>Donnerstag</th><th>Freitag</th></tr>
    <tr><td class="time">Ab 7:30</td><td>Blutentnahme/ Ultraschall</td><td>Blutentnahme/ Ultraschall</td><td>Blutentnahme/ Ultraschall</td><td>Blutentnahme/ Ultraschall</td><td>Blutentnahme/ Ultraschall</td></tr>
    <tr><td class="time">8:00-09:00</td><td class="free">Freie Sprechstunde</td><td class="free">Freie Sprechstunde</td><td class="free">Freie Sprechstunde</td><td class="free">Freie Sprechstunde</td><td class="free">Freie Sprechstunde</td></tr>
    <tr><td class="time">9:00-10:00</td><td class="free">Freie Sprechstunde</td><td class="free">Freie Sprechstunde</td><td class="free">Freie Sprechstunde</td><td class="free">Freie Sprechstunde</td><td class="free">Freie Sprechstunde</td></tr>
    <tr><td class="time">10:00-11:00</td><td class="free">Freie Sprechstunde</td><td class="free">Freie Sprechstunde</td><td class="free">Freie Sprechstunde</td><td class="free">Freie Sprechstunde</td><td class="free">Freie Sprechstunde</td></tr>
    <tr><td class="time">11:00-12:00</td><td class="free">Freie Sprechstunde</td><td class="free">Freie Sprechstunde</td><td class="free">Freie Sprechstunde</td><td class="free">Freie Sprechstunde</td><td class="free">Freie Sprechstunde</td></tr>
    <tr><td class="time">12:00-13:00</td><td class="visit">Hausbesuche</td><td class="visit">Hausbesuche</td><td class="visit">Hausbesuche</td><td class="visit">Hausbesuche</td><td class="visit">Hausbesuche</td></tr>
    <tr><td class="time">13:00-15:30</td><td>Mittagspause</td><td>Mittagspause</td><td>Mittagspause</td><td>Mittagspause</td><td>Mittagspause</td></tr>
    <tr><td class="time">15:30-16:00</td><td class="appt">Termin-Sprechstunde</td><td class="appt">Termin-Sprechstunde</td><td class="appt">Termin-Sprechstunde</td><td class="appt">Termin-Sprechstunde</td><td class="appt">Termin-Sprechstunde</td></tr>
    <tr><td class="time">16:00-17:00</td><td class="free">Freie Sprechstunde</td><td class="free">Freie Sprechstunde</td><td></td><td class="free">Freie Sprechstunde</td><td></td></tr>
    <tr><td class="time">17:00-18:00</td><td class="free">Freie Sprechstunde</td><td class="free">Freie Sprechstunde</td><td></td><td class="free">Freie Sprechstunde</td><td></td></tr>
  </table>
</section>

<div class="address-card">
  <svg width="22" height="32" viewBox="0 0 22 32" style="margin-top:28px"><path d="M11 0C4.9 0 0 4.9 0 11c0 8 11 21 11 21s11-13 11-21C22 4.9 17.1 0 11 0z" fill="#1f2e5c"/><circle cx="11" cy="11" r="4.5" fill="#8aa0c8"/></svg>
  <h3>Adresse</h3>
  <p>Ihre Adresse<br>Stadt<br>Deutschland<br>Telefonnummer</p>
</div>

<section class="cta">
  <p class="cta-text">Möchten Sie einen Termin vereinbaren?</p>
  <a class="btn btn-call">Anrufen</a>
  <a class="btn btn-mail">E-Mail schreiben</a>
</section>

<footer class="site-footer">
  <ul class="contact-list">
    <li><svg width="12" height="12" viewBox="0 0 12 12"><path d="M2 0h3l1 3-2 1.5c.8 1.6 2 2.8 3.5 3.5L9 6l3 1v3c0 1-1 2-2 2C4.5 12 0 7.5 0 2 0 1 1 0 2 0z" fill="#333"/></svg>0049-30-5557214</li>
    <li><svg width="12" height="12" viewBox="0 0 12 12"><path d="M12 0L0 5l4.5 1.5L6 12z" fill="none" stroke="#333"/></svg>kontakt@praxis-lindenhof.de</li>
    <li><svg width="12" height="12" viewBox="0 0 12 12"><rect x="1.5" y="0.5" width="9" height="11" fill="none" stroke="#333"/><rect x="3.5" y="2.5" width="2" height="2" fill="#333"/><rect x="6.5" y="2.5" width="2" height="2" fill="#333"/><rect x="3.5" y="6" width="2" height="2" fill="#333"/><rect x="6.5" y="6" width="2" height="2" fill="#333"/></svg>Lindenallee 48, Berlin</li>
  </ul>
  <div class="footer-col" style="right:449px">
    <h4>LINKS</h4>
    <ul><li>Startseite</li><li>Team</li><li>Öffnungszeiten</li><li>Kontakt</li></ul>
  </div>
  <div class="footer-col" style="right:134px">
    <h4>WICHTIGES</h4>
    <ul><li>Datenschutzrichtlinien</li><li>Impressum</li></ul>
  </div>
</footer>

</div>
</body>
</html>
```